Brimwell Music Studio needs a promotional postcard design

We are looking for a postcard design for a small business that provides clients with private music lesson instruction. We are looking for a design that will convey the message of "music is fun for kids" that will appeal to parents and encourage them to sign up. We have a company logo that should be used and our color scheme is teal and turquoise. All of our contact info should be displayed as well.

Target Market(s)

Parents with young kids

Contact Information for Business Card

web: www.brimwellmusicstudio.example
email: lessons@brimwellmusicstudio.example
phone: 202-555-0147

Font styles to use
Serif
Sans Serif

Colors
33b8a4
86cfc6
0456a4
87cfc6

Requirements
Must have
• Music lessons in your home
• Creating little stars one at a time
• Sign Up Now
• Please use these images:
Nice to have
• Something like this sample postcard:

```html
<!DOCTYPE html>
<html lang="en">
<head>
<meta charset="utf-8">
<title>Brimwell Music Studio – Postcard</title>
<link href="https://fonts.googleapis.com/css2?family=Mali:wght@500&family=Rokkitt:wght@500;700&family=Roboto:wght@400&family=Tinos&display=swap" rel="stylesheet">
<style>
  :root {
    --page-bg: #ececec;
    --card-bg: #f2f2f2;
    --teal: #4fbcc0;
    --blue: #1b6db5;
    --blue-deep: #1760a8;
    --photo-dark: #2a2a2e;
    --photo-mid: #6b4d3e;
    --photo-light: #c9a58f;
    --ink: #3a3a3a;
  }
  * { margin: 0; padding: 0; box-sizing: border-box; }
  html, body { width: 1200px; height: 1000px; overflow: hidden; background: var(--page-bg); }
  .postcard {
    position: absolute; left: 165px; top: 192px;
    width: 870px; height: 615px;
    background: var(--card-bg);
    overflow: hidden;
  }
  .postcard__art { position: absolute; left: 0; top: 0; width: 440px; height: 615px; }
  .postcard__content { position: absolute; right: 24px; top: 0; width: 460px; height: 615px; text-align: right; }
  .tagline {
    position: absolute; right: 0; top: 24px;
    font-family: "Mali", cursive; font-weight: 500;
    font-size: 36px; color: var(--blue); white-space: nowrap;
  }
  .headline {
    position: absolute; right: 0; top: 88px;
    font-family: "Rokkitt", serif; font-weight: 700;
    font-size: 168px; line-height: 1; letter-spacing: 2px; white-space: nowrap;
  }
  .headline .teal { color: var(--teal); }
  .headline .blue { color: var(--blue); }
  .subhead {
    position: absolute; right: 0; top: 252px;
    font-family: "Rokkitt", serif; font-weight: 700;
    font-size: 36px; color: var(--blue-deep); white-space: nowrap;
  }
  .brand { position: absolute; right: 0; top: 340px; display: flex; align-items: center; gap: 24px; }
  .brand__dot { width: 70px; height: 70px; border-radius: 50%; background: var(--teal); }
  .brand__name {
    font-family: "Tinos", serif; font-size: 23px; line-height: 28px;
    color: var(--teal); text-align: left; width: 120px;
  }
  .cta {
    position: absolute; right: 0; top: 472px;
    font-family: "Rokkitt", serif; font-weight: 500;
    font-size: 50px; color: var(--blue); white-space: nowrap;
  }
  .contact {
    position: absolute; right: 0; top: 536px; list-style: none;
    font-family: "Roboto", sans-serif; font-size: 15.5px; line-height: 21px; color: var(--ink);
  }
</style>
</head>
<body>
  <main class="postcard">
    <svg class="postcard__art" viewBox="0 0 440 615" aria-hidden="false">
      <defs>
        <linearGradient id="photoTone" x1="0" y1="0" x2="0" y2="1">
          <stop offset="0" stop-color="var(--photo-mid)"/>
          <stop offset="0.35" stop-color="var(--photo-light)"/>
          <stop offset="0.55" stop-color="var(--photo-dark)"/>
          <stop offset="1" stop-color="var(--photo-dark)"/>
        </linearGradient>
      </defs>
      <path class="art__band-blue" d="M0 0 H226 V40 C150 40 90 70 60 130 C40 175 20 190 0 195 Z" fill="var(--blue)"/>
      <path class="art__band-teal" d="M0 360 C30 380 40 420 45 480 C50 540 55 580 60 615 H0 Z" fill="var(--teal)"/>
      <g role="img" aria-label="Photo of a smiling young girl making a peace sign, cut out with a white outline">
        <path d="M58 615 C52 540 50 470 40 410 C30 360 10 330 0 300 V215 C40 200 70 180 90 130 C110 80 150 50 210 48 C270 46 320 80 335 150 C350 210 370 300 400 390 C415 440 395 470 380 500 C395 540 400 580 402 615 Z" fill="#ffffff"/>
        <path d="M70 615 C64 540 62 470 52 410 C42 360 20 330 8 300 V225 C48 210 80 188 100 140 C120 92 155 62 210 60 C265 58 308 90 322 152 C336 212 356 300 386 390 C398 436 380 466 366 500 C382 540 386 580 388 615 Z" fill="url(#photoTone)"/>
      </g>
    </svg>

    <section class="postcard__content">
      <p class="tagline">Creating little stars one at a time</p>
      <h1 class="headline"><span class="teal">M</span><span class="blue">u</span><span class="teal">s</span><span class="blue">i</span><span class="teal">c</span></h1>
      <p class="subhead">Lessons In Your Home!</p>
      <div class="brand">
        <span class="brand__dot" aria-hidden="true"></span>
        <p class="brand__name">Brimwell Music Studio</p>
      </div>
      <p class="cta">Sign Up Now</p>
      <ul class="contact">
        <li>202-555-0147</li>
        <li>www.brimwellmusicstudio.example</li>
        <li>lessons@brimwellmusicstudio.example</li>
      </ul>
    </section>
  </main>
</body>
</html>
```